Professional Business Card for Luxury Hotel & Resort Development Firm. Advisory firm

Project Overview: We are a specialized advisory firm focused on Hotel & Resort Development. Our clients are high-net-worth investors and major hospitality brands.

Design Requirements:

Style: Minimalist, sophisticated, and trustworthy. We want to avoid looking too "corporate" or "dry"—it should feel premium.

Key Elements: Please incorporate our logo [もしロゴがあれば] and emphasize a clean layout with plenty of white space.

Color Palette: We prefer Grey and White or Black and White to evoke a sense of luxury and stability.

Typography: Professional garamond, or sans-serif or elegant serif fonts

Goal: The card should feel substantial and high-end when handed to a client, reflecting our expertise in multi-million dollar developments.

I am currently on a business trip for field research and have limited access to my desktop. Additionally, I have just provided detailed technical feedback to a designer and am waiting for their refined proposals. To ensure the final logo meets the high standards of my new advisory firm, I would like to extend the deadline by 7 days. Thank you for your support.

Target Market(s)

High-net-worth investors, luxury hospitality brands, and real estate developers.

Contact Information for Business Card

Firm Name: Corvale Advisory Group, My Name: Kenshiro Fujisawa, Title: Founder, Address 5-8-4 Kitahoshino Midori Yokohama Japan 226-0071, email address: kfujisawa@corvaleadvisoryx.com, Tel: +81 80-4217-3058. Front Site (Primary): Japanese translation of the back side, Please use a clean Japanese font (like Mincho) that complements the Garmond on the English side Back side: English. Note for Japanese text: since the frond side is the main fae, please ensure the layout is clean and professional. Please use a high-quality Mincho ( Serif-style) font for Japanese to mach the Garmond used on the English side. Text for Front side (Japanese) Corvale Advisory Group, 役職:代表、藤沢謙志郎、226-0071 横浜市緑区北星野5-8-4. Name of the firm can stay in English.

Other font styles liked:
• Font Preference: Please use Garamond for all text to maintain a consistent, elegant, and classic professional look.

Requirements
Must have
• Professional and clean layout, high-end feel.
Nice to have
• Minimalist design with subtle luxury accents.

```html
<!DOCTYPE html>
<html lang="ja">
<head>
<meta charset="utf-8">
<title>Corvale Advisory Group — Business Card</title>
<link rel="stylesheet" href="https://fonts.googleapis.com/css2?family=EB+Garamond:wght@400;500;600&family=Shippori+Mincho:wght@400;500&display=swap">
<style>
  :root {
    --backdrop: #3a3a3a;
    --card: #121212;
    --ink-light: #f4f4f2;
    --ink-muted: #d6d6d4;
    --band: #ffffff;
    --ink-dark: #111111;
    --serif: "EB Garamond", Garamond, serif;
    --mincho: "Shippori Mincho", "Hiragino Mincho ProN", serif;
  }
  * { box-sizing: border-box; margin: 0; padding: 0; }
  html, body { width: 1200px; height: 689px; overflow: hidden; }
  body {
    background: var(--backdrop);
    display: flex;
    align-items: center;
    justify-content: center;
    gap: 40px;
  }
  .card {
    position: relative;
    width: 540px;
    height: 327px;
    background: var(--card);
    border-radius: 22px;
    color: var(--ink-light);
    overflow: hidden;
    box-shadow: 0 18px 40px rgba(0,0,0,.45);
  }

  /* Front — Japanese */
  .card-front {
    display: flex;
    flex-direction: column;
    align-items: center;
    padding-top: 44px;
    font-family: var(--mincho);
  }
  .front-firm {
    font-family: var(--serif);
    font-weight: 600;
    font-size: 38px;
    letter-spacing: 1px;
  }
  .front-title { margin-top: 12px; font-size: 18px; color: var(--ink-muted); }
  .front-name { margin-top: 4px; font-size: 36px; letter-spacing: 6px; }
  .front-postal { margin-top: 26px; font-size: 20px; }
  .front-address { margin-top: 4px; font-size: 22px; letter-spacing: 1px; }

  /* Back — English */
  .card-back { font-family: var(--serif); }
  .back-firm {
    position: absolute;
    left: 30px;
    top: 54px;
    font-size: 46px;
    font-weight: 600;
    letter-spacing: 1.5px;
    white-space: nowrap;
  }
  .back-person {
    position: absolute;
    left: 30px;
    top: 158px;
    width: 244px;
    text-align: right;
  }
  .back-name { font-size: 25px; font-weight: 600; letter-spacing: .5px; }
  .back-role { font-size: 19px; color: var(--ink-muted); letter-spacing: 1px; }
  .back-divider {
    position: absolute;
    left: 290px;
    top: 156px;
    width: 1.5px;
    height: 66px;
    background: var(--ink-light);
  }
  .back-contacts {
    position: absolute;
    left: 306px;
    top: 158px;
    list-style: none;
    font-size: 13.5px;
  }
  .contact-item { display: flex; align-items: center; gap: 8px; height: 30px; }
  .contact-icon { width: 20px; height: 20px; flex: none; }
  .back-band {
    position: absolute;
    left: 0;
    right: 0;
    top: 258px;
    height: 32px;
    background: var(--band);
    color: var(--ink-dark);
    display: flex;
    align-items: center;
    gap: 8px;
    padding-left: 40px;
    font-size: 14.5px;
  }
  .band-icon { width: 18px; height: 18px; flex: none; }
</style>
</head>
<body>

  <section class="card card-front" aria-label="Front side, Japanese">
    <p class="front-firm">Corvale Advisory Group</p>
    <p class="front-title">役職：代表</p>
    <p class="front-name">藤沢 謙志郎</p>
    <p class="front-postal">〒226-0071</p>
    <p class="front-address">横浜市緑区北星野5-8-4</p>
  </section>

  <section class="card card-back" aria-label="Back side, English">
    <p class="back-firm">Corvale Advisory Group</p>
    <div class="back-person">
      <p class="back-name">Kenshiro Fujisawa</p>
      <p class="back-role">Founder</p>
    </div>
    <span class="back-divider"></span>
    <ul class="back-contacts">
      <li class="contact-item">
        <svg class="contact-icon" viewBox="0 0 20 20" aria-hidden="true">
          <circle cx="10" cy="10" r="10" fill="#f4f4f2"/>
          <path d="M6.2 5.2l2 0 .9 2.4-1.2.9a7 7 0 0 0 3.6 3.6l.9-1.2 2.4.9 0 2a1 1 0 0 1-1.1 1A9 9 0 0 1 5.2 6.3a1 1 0 0 1 1-1.1z" fill="#121212"/>
        </svg>
        <span>+81 80-4217-3058</span>
      </li>
      <li class="contact-item">
        <svg class="contact-icon" viewBox="0 0 20 20" aria-hidden="true">
          <circle cx="10" cy="10" r="10" fill="#f4f4f2"/>
          <rect x="5" y="6.5" width="10" height="7" rx="1" fill="#121212"/>
          <path d="M5.4 7l4.6 3.6L14.6 7" fill="none" stroke="#f4f4f2" stroke-width="1"/>
        </svg>
        <span>kfujisawa@corvaleadvisoryx.com</span>
      </li>
    </ul>
    <div class="back-band">
      <svg class="band-icon" viewBox="0 0 18 18" aria-hidden="true">
        <circle cx="9" cy="9" r="9" fill="#111111"/>
        <path d="M9 3.6a3.6 3.6 0 0 1 3.6 3.6c0 2.6-3.6 6.8-3.6 6.8S5.4 9.8 5.4 7.2A3.6 3.6 0 0 1 9 3.6z" fill="#ffffff"/>
        <circle cx="9" cy="7.2" r="1.4" fill="#111111"/>
      </svg>
      <span>5-8-4 Kitahoshino Midori, Yokohama Japan 226-0071</span>
    </div>
  </section>

</body>
</html>
```